Alder Hollow Family Dentistry
business card
Alder Hollow Family Dentistry -
Creative Brief
Simple
Dr. Owen T. Farrow, D.M.D.
2817 Juniper Ln. Ste. C South Ogden, UT 84561
drfarrow@alderhollowfamilydentistry.example
www.alderhollowfamilydentistry.example

```html
<!DOCTYPE html>
<html lang="en">
<head>
<meta charset="utf-8">
<title>Alder Hollow Family Dentistry – Stationery</title>
<link href="https://fonts.googleapis.com/css2?family=Open+Sans:wght@400;600;700&display=swap" rel="stylesheet">
<style>
  :root{
    --bg:#e6e6e6;
    --paper:#ffffff;
    --navy:#1f3f7a;
    --blue:#3d6fc4;
    --blue-deep:#2a55a8;
    --sky:#a9c3ec;
    --green:#8cc63f;
    --ink:#333d4d;
    --rule:#9aa3b2;
    --mist:#e9eef7;
  }
  *{box-sizing:border-box;margin:0;padding:0}
  html,body{width:1200px;height:552px;overflow:hidden}
  body{background:var(--bg);font-family:"Open Sans",Arial,sans-serif;color:var(--ink);position:relative}
  .piece{position:absolute;background:var(--paper);box-shadow:0 1px 4px rgba(0,0,0,.18);overflow:hidden}
  .wave{position:absolute;left:0;bottom:0;width:100%}
  .brand{position:absolute;font-weight:700;color:var(--navy);line-height:1.15;display:flex;align-items:center;gap:5px}
  .brand .dot{width:8px;height:8px;border-radius:50%;background:var(--green);flex:none}
  .brand.light{color:#fff}
  .contact{position:absolute;list-style:none;font-size:5px;line-height:7.5px;color:var(--ink)}
  .contact li{display:flex;align-items:center;gap:3px}
  .contact li::before{content:"";width:3.5px;height:3.5px;background:var(--blue);border-radius:50%}
  .mist{position:absolute;background:radial-gradient(ellipse at 50% 70%,var(--mist),rgba(255,255,255,0) 70%)}

  /* sheets */
  .sheet{top:24px;width:355px;height:509px}
  .fax{left:29px}
  .letterhead{left:403px}
  .sheet .brand{left:24px;top:30px;font-size:11px}
  .sheet .contact{right:26px;top:24px}
  .sheet .mist{left:110px;top:330px;width:140px;height:70px}

  .fax-title{position:absolute;right:30px;top:70px;font-size:8px;font-weight:700;color:var(--navy)}
  .fax-table{position:absolute;left:22px;top:82px;width:310px;border-collapse:collapse;font-size:6px}
  .fax-table td{border:1px solid var(--rule);height:20px;padding:0 4px}
  .fax-table .label{width:60px;color:var(--ink)}
  .fax-checks{position:absolute;left:22px;top:184px;width:310px;display:flex;justify-content:space-between;font-size:5.5px}
  .fax-checks span{display:flex;align-items:center;gap:3px}
  .fax-checks span::before{content:"";width:6px;height:6px;border:1px solid var(--rule)}

  /* cards */
  .card{top:24px;width:144px;height:74px}
  .card-front{left:775px}
  .card-front .brand{left:8px;top:8px;font-size:6px;gap:3px}
  .card-front .brand .dot{width:5px;height:5px}
  .card-front .person{position:absolute;left:72px;top:22px;font-size:4.2px;font-weight:700;color:var(--navy)}
  .card-front .contact{left:72px;top:29px;font-size:3.4px;line-height:5px}
  .card-front .contact li::before{width:2.5px;height:2.5px}
  .card-back{left:933px;background:linear-gradient(160deg,var(--sky),var(--blue) 55%,var(--blue-deep))}
  .card-back .brand{left:30px;top:28px;font-size:7px}

  /* envelopes */
  .envelope{left:775px;width:401px}
  .env-front{top:125px;height:192px}
  .env-front .brand{left:16px;top:16px;font-size:9px}
  .env-front .contact{left:22px;top:44px;font-size:4.5px;line-height:7px}
  .env-front .mist{left:135px;top:78px;width:130px;height:60px}
  .env-back{top:336px;height:197px;background:linear-gradient(180deg,#fff 0%,#f4f7fc 30%,var(--sky) 60%,var(--blue) 85%,var(--blue-deep))}
  .env-back .flap{position:absolute;inset:0;width:100%;height:100%}
  .env-back .brand{left:150px;top:92px;font-size:9px}
</style>
</head>
<body>

<!-- Fax sheet -->
<section class="piece sheet fax">
  <div class="brand"><span class="dot"></span>Alder Hollow<br>Family Dentistry</div>
  <ul class="contact">
    <li>2817 Juniper Ln. Ste. C</li>
    <li>South Ogden, UT 84561</li>
    <li>drfarrow@alderhollowfamilydentistry.example</li>
    <li>www.alderhollowfamilydentistry.example</li>
  </ul>
  <div class="fax-title">FAX</div>
  <table class="fax-table">
    <tr><td class="label">To:</td><td></td><td class="label">From:</td><td></td></tr>
    <tr><td class="label">Fax:</td><td></td><td class="label">Pages:</td><td></td></tr>
    <tr><td class="label">Phone:</td><td></td><td class="label">Date:</td><td></td></tr>
    <tr><td class="label">Re:</td><td></td><td class="label">CC:</td><td></td></tr>
  </table>
  <div class="fax-checks">
    <span>Urgent</span><span>For Review</span><span>Please Comment</span><span>Please Reply</span><span>Please Recycle</span>
  </div>
  <div class="mist" role="img" aria-label="Faint mountain range backdrop"></div>
  <svg class="wave" viewBox="0 0 355 120" height="120" preserveAspectRatio="none" aria-hidden="true">
    <defs><linearGradient id="wg1" x1="0" y1="0" x2="0" y2="1"><stop offset="0" stop-color="#c6d7f2"/><stop offset="1" stop-color="#3d6fc4"/></linearGradient></defs>
    <path d="M0 55 C90 25 200 40 355 20 L355 120 L0 120Z" fill="url(#wg1)"/>
    <path d="M0 48 C90 18 200 33 355 12" fill="none" stroke="#8cc63f" stroke-width="3"/>
    <path d="M0 42 C100 14 210 26 355 6" fill="none" stroke="#a9c3ec" stroke-width="1.2"/>
  </svg>
</section>

<!-- Letterhead -->
<section class="piece sheet letterhead">
  <div class="brand"><span class="dot"></span>Alder Hollow<br>Family Dentistry</div>
  <ul class="contact">
    <li>2817 Juniper Ln. Ste. C</li>
    <li>South Ogden, UT 84561</li>
    <li>drfarrow@alderhollowfamilydentistry.example</li>
    <li>www.alderhollowfamilydentistry.example</li>
  </ul>
  <div class="mist" role="img" aria-label="Faint mountain range backdrop"></div>
  <svg class="wave" viewBox="0 0 355 120" height="120" preserveAspectRatio="none" aria-hidden="true">
    <defs><linearGradient id="wg2" x1="0" y1="0" x2="0" y2="1"><stop offset="0" stop-color="#c6d7f2"/><stop offset="1" stop-color="#3d6fc4"/></linearGradient></defs>
    <path d="M0 55 C90 25 200 40 355 20 L355 120 L0 120Z" fill="url(#wg2)"/>
    <path d="M0 48 C90 18 200 33 355 12" fill="none" stroke="#8cc63f" stroke-width="3"/>
    <path d="M0 42 C100 14 210 26 355 6" fill="none" stroke="#a9c3ec" stroke-width="1.2"/>
  </svg>
</section>

<!-- Business card front -->
<section class="piece card card-front">
  <div class="brand"><span class="dot"></span>Alder Hollow<br>Family Dentistry</div>
  <div class="person">Dr. Owen T. Farrow, D.M.D.</div>
  <ul class="contact">
    <li>2817 Juniper Ln. Ste. C</li>
    <li>South Ogden, UT 84561</li>
    <li>drfarrow@alderhollowfamilydentistry.example</li>
    <li>www.alderhollowfamilydentistry.example</li>
  </ul>
  <svg class="wave" viewBox="0 0 144 20" height="20" preserveAspectRatio="none" aria-hidden="true">
    <path d="M0 12 C40 4 90 10 144 3 L144 20 L0 20Z" fill="#3d6fc4"/>
    <path d="M0 10 C40 2 90 8 144 1" fill="none" stroke="#8cc63f" stroke-width="1.2"/>
  </svg>
</section>

<!-- Business card back -->
<section class="piece card card-back">
  <div class="brand light"><span class="dot"></span>Alder Hollow<br>Family Dentistry</div>
</section>

<!-- Envelope front -->
<section class="piece envelope env-front">
  <div class="brand"><span class="dot"></span>Alder Hollow<br>Family Dentistry</div>
  <ul class="contact">
    <li>2817 Juniper Ln. Ste. C</li>
    <li>South Ogden, UT 84561</li>
    <li>www.alderhollowfamilydentistry.example</li>
  </ul>
  <div class="mist" role="img" aria-label="Faint mountain range backdrop"></div>
  <svg class="wave" viewBox="0 0 401 60" height="60" preserveAspectRatio="none" aria-hidden="true">
    <defs><linearGradient id="wg3" x1="0" y1="0" x2="0" y2="1"><stop offset="0" stop-color="#c6d7f2"/><stop offset="1" stop-color="#3d6fc4"/></linearGradient></defs>
    <path d="M0 30 C110 10 240 22 401 8 L401 60 L0 60Z" fill="url(#wg3)"/>
    <path d="M0 25 C110 5 240 17 401 3" fill="none" stroke="#8cc63f" stroke-width="2.5"/>
  </svg>
</section>

<!-- Envelope back -->
<section class="piece envelope env-back">
  <svg class="flap" viewBox="0 0 401 197" preserveAspectRatio="none" aria-hidden="true">
    <path d="M0 0 L200 80 L401 0" fill="none" stroke="#c9d3e3" stroke-width="1"/>
  </svg>
  <div class="brand light"><span class="dot"></span>Alder Hollow<br>Family Dentistry</div>
</section>

</body>
</html>
```